Meadow Crate Co came about when a life change having to do with my health became an issue and I had to change my diet. We’re a homeschool family and learned a more simplistic way to eat and live out our day to day. We’re ready to share how we eat. Included are attachments to give a visual to the concepts in mind. The first attachment is the logo the second is basically the main idea of the company referencing to getting to the roots of nutrition and juicing. The roots design CONCEPT would be incorporated onto the bottle label. The third attachment is representing the clear stickers we’d like to have on bottles. The 4th and Last are the bottle design we’re looking to use. We’d like tall cylinder bottles.

Label must haves :
meadow crate co logo and the quote know your roots
The roots design
MeadowCrateCo.example

```html
<!DOCTYPE html>
<html lang="en">
<head>
<meta charset="utf-8">
<title>Meadow Crate Co – Know Your Roots bottle label</title>
<link rel="stylesheet" href="https://fonts.googleapis.com/css2?family=Poppins:wght@400;500;800&display=swap">
<style>
  :root {
    --juice-amber: #d9ae3a;
    --juice-deep: #b8891f;
    --ink: #111111;
    --roots-shade: rgba(40, 28, 6, 0.45);
    --label-text-light: #f3e2a6;
  }
  * { margin: 0; padding: 0; box-sizing: border-box; }
  html, body { width: 800px; height: 1200px; overflow: hidden; }
  body {
    background: linear-gradient(180deg, var(--juice-amber) 0%, var(--juice-deep) 55%, var(--juice-amber) 100%);
    font-family: "Poppins", sans-serif;
    color: var(--ink);
  }
  .label {
    position: relative;
    width: 800px;
    height: 1200px;
  }
  .brand {
    position: absolute;
    top: 150px;
    left: 0;
    width: 800px;
    display: flex;
    align-items: center;
    justify-content: center;
    gap: 18px;
  }
  .brand__dot {
    width: 46px;
    height: 46px;
    border-radius: 50%;
    background: var(--ink);
  }
  .brand__name {
    font-weight: 800;
    font-size: 46px;
    line-height: 1;
    letter-spacing: 0.5px;
  }
  .roots-art {
    position: absolute;
    top: 340px;
    left: 150px;
    width: 500px;
    height: 490px;
    border-radius: 24px;
    background: radial-gradient(ellipse at 50% 62%, var(--roots-shade) 0%, rgba(40, 28, 6, 0.22) 55%, rgba(40, 28, 6, 0.08) 100%);
  }
  .tagline {
    position: absolute;
    top: 860px;
    left: 0;
    width: 800px;
    text-align: center;
    font-size: 50px;
    line-height: 62px;
    letter-spacing: 12px;
    text-indent: 12px;
  }
  .tagline__word { display: block; font-weight: 400; }
  .tagline__word--strong { font-weight: 800; }
  .web-bar {
    position: absolute;
    top: 1070px;
    left: 215px;
    width: 370px;
    height: 52px;
    background: var(--ink);
    color: var(--label-text-light);
    font-weight: 500;
    font-size: 19px;
    letter-spacing: 3px;
    display: flex;
    align-items: center;
    justify-content: center;
  }
</style>
</head>
<body>
  <main class="label">
    <header class="brand">
      <span class="brand__dot"></span>
      <span class="brand__name">Meadow Crate Co</span>
    </header>

    <div class="roots-art" role="img" aria-label="Line illustration of a sprout whose stem runs into a bottle outline and branches into roots shaped like a pair of lungs"></div>

    <h1 class="tagline">
      <span class="tagline__word">KNOW</span>
      <span class="tagline__word tagline__word--strong">YOUR</span>
      <span class="tagline__word">ROOTS</span>
    </h1>

    <p class="web-bar">MeadowCrateCo.example</p>
  </main>
</body>
</html>
```